Professional/Sleek card design for athletic apparel brand

Athletic apparel brand. Mainly focused on lifting weights/gym workouts. Logo and brand are already created. Must use brand logo and name. Creativity is welcome. Looking for a clean, modern, and sexy design.

```html
<!DOCTYPE html>
<html lang="en">
<head>
<meta charset="utf-8">
<title>Iron and Grit — Business Card</title>
<link href="https://fonts.googleapis.com/css2?family=Montserrat:wght@400;500;800&display=swap" rel="stylesheet">
<style>
  :root {
    --backdrop: #2b2d31;
    --card-light: #ffffff;
    --card-dark: #262626;
    --ink: #111111;
    --ink-soft: #555555;
    --mark-faint: #3a3a3a;
    --paper-light: #f2f2f2;
  }
  * { margin: 0; padding: 0; box-sizing: border-box; }
  html, body {
    width: 1200px; height: 952px; overflow: hidden;
    background: radial-gradient(ellipse at 55% 40%, #3c3e43 0%, var(--backdrop) 70%);
    font-family: "Montserrat", sans-serif;
  }
  .canvas { position: relative; width: 1200px; height: 952px; }

  .card {
    position: absolute;
    border-radius: 22px;
    overflow: hidden;
    box-shadow: 0 18px 40px rgba(0,0,0,.45);
  }

  /* Front: contact side */
  .card-front {
    left: 560px; top: 150px; width: 540px; height: 310px;
    background: var(--card-light);
    color: var(--ink);
  }
  .front-brand {
    position: absolute; left: 0; top: 0; width: 210px; height: 100%;
    display: flex; align-items: center; justify-content: center; gap: 10px;
  }
  .brand-dot {
    width: 14px; height: 14px; border-radius: 50%; background: var(--ink);
  }
  .brand-name {
    font-weight: 800; font-size: 22px; line-height: 1.05;
    text-transform: uppercase; letter-spacing: .5px;
  }
  .front-divider {
    position: absolute; left: 210px; top: 0; width: 60px; height: 100%;
    background: linear-gradient(90deg, rgba(0,0,0,.08), rgba(0,0,0,0));
  }
  .front-details { position: absolute; left: 250px; top: 62px; right: 30px; }
  .person-name { font-size: 21px; letter-spacing: .5px; font-weight: 500; }
  .person-name b { font-weight: 800; }
  .person-role {
    font-size: 12px; color: var(--ink-soft); margin-top: 3px;
    padding-bottom: 8px; border-bottom: 1px solid #999; width: 170px;
  }
  .contact-list { list-style: none; margin-top: 14px; }
  .contact-list li {
    display: flex; align-items: flex-start; gap: 10px;
    font-size: 12px; color: var(--ink-soft); margin-bottom: 9px; line-height: 1.35;
  }
  .contact-icon {
    flex: none; width: 18px; height: 18px; border-radius: 4px;
    background: var(--ink); display: flex; align-items: center; justify-content: center;
  }
  .contact-icon svg { width: 11px; height: 11px; fill: #fff; }

  /* Back: brand side */
  .card-back {
    left: 170px; top: 300px; width: 310px; height: 540px;
    background: var(--card-dark);
    color: var(--paper-light);
  }
  .back-brand {
    position: absolute; top: 90px; left: 0; right: 0; text-align: center;
  }
  .back-brand .brand-name { font-size: 30px; color: var(--paper-light); }
  .back-brand .brand-rule {
    width: 130px; height: 1px; background: #777; margin: 8px auto;
  }
  .back-mark {
    position: absolute; left: 40px; top: 250px; width: 360px; height: 360px;
    border-radius: 50%; background: var(--mark-faint);
  }
</style>
</head>
<body>
<main class="canvas">

  <section class="card card-back">
    <div class="back-brand">
      <div class="brand-name">Iron</div>
      <div class="brand-rule"></div>
      <div class="brand-name">Grit</div>
    </div>
    <div class="back-mark" aria-hidden="true"></div>
  </section>

  <section class="card card-front">
    <div class="front-brand">
      <span class="brand-dot"></span>
      <span class="brand-name">Iron and<br>Grit</span>
    </div>
    <div class="front-divider"></div>
    <div class="front-details">
      <h1 class="person-name">DANIEL R. <b>HARLOW</b></h1>
      <p class="person-role">Managing Director</p>
      <ul class="contact-list">
        <li>
          <span class="contact-icon"><svg viewBox="0 0 24 24"><path d="M12 2a7 7 0 0 0-7 7c0 5 7 13 7 13s7-8 7-13a7 7 0 0 0-7-7zm0 9.5A2.5 2.5 0 1 1 12 6.5a2.5 2.5 0 0 1 0 5z"/></svg></span>
          <span>48 Foundry Lane Eastwood<br>Park NSW 000 USA</span>
        </li>
        <li>
          <span class="contact-icon"><svg viewBox="0 0 24 24"><path d="M6.6 10.8a15 15 0 0 0 6.6 6.6l2.2-2.2a1 1 0 0 1 1-.25 11 11 0 0 0 3.6.6 1 1 0 0 1 1 1V20a1 1 0 0 1-1 1A17 17 0 0 1 3 4a1 1 0 0 1 1-1h3.5a1 1 0 0 1 1 1c0 1.25.2 2.45.6 3.6a1 1 0 0 1-.25 1z"/></svg></span>
          <span>+00 987 654 32</span>
        </li>
        <li>
          <span class="contact-icon"><svg viewBox="0 0 24 24"><path d="M2 5h20v14H2zm2 2v.5l8 5 8-5V7l-8 5z"/></svg></span>
          <span>hello@ironandgrit.com</span>
        </li>
        <li>
          <span class="contact-icon"><svg viewBox="0 0 24 24"><path d="M12 2a10 10 0 1 0 0 20 10 10 0 0 0 0-20zm6.9 9h-3a15 15 0 0 0-1.3-5.6A8 8 0 0 1 18.9 11zM12 4c.9 1.3 1.7 3.9 1.9 7h-3.8c.2-3.1 1-5.7 1.9-7zM4.1 13h3a15 15 0 0 0 1.3 5.6A8 8 0 0 1 4.1 13zm3-2h-3a8 8 0 0 1 4.3-5.6A15 15 0 0 0 7.1 11zM12 20c-.9-1.3-1.7-3.9-1.9-7h3.8c-.2 3.1-1 5.7-1.9 7zm2.6-1.4a15 15 0 0 0 1.3-5.6h3a8 8 0 0 1-4.3 5.6z"/></svg></span>
          <span>www.ironandgrit.com</span>
        </li>
      </ul>
    </div>
  </section>

</main>
</body>
</html>
```